Law firm Seeks Modern and Engaging Site Redesign

Law firm seeks a new web site. Should be modern, but retaining existing logo. Needs to include contact section, professional bio, services offered, and contact information.

The site should be modern, responsive, and able to be SEO optimized.

The finished product should be coded in a Wordpress site, which I will provide. I can work with other platforms, including Wix, but WP is preferred.

Note the current site is https://www.tallowfieldlaw.example/#/home

Target Market(s)

Family Law Practice

Industry/Entity Type

Legal

Coding

Coded - Design and coding required

Number of Pages Required

4 page

Font styles to use
Sans Serif

Requirements
Must have
• Service description
Bio pages for partners
Contact Form
Awards/Publication page

```html
<!DOCTYPE html>
<html lang="en">
<head>
<meta charset="utf-8">
<title>Tallow Field – Attorneys at Law</title>
<link href="https://fonts.googleapis.com/css2?family=Lato:wght@300;400;700&display=swap" rel="stylesheet">
<style>
:root{
  --blue:#4a5cc4;
  --blue-dark:#3b4db3;
  --ink:#444;
  --muted:#8a8a8a;
  --light:#f5f5f5;
  --nav:#5b5b5b;
  --footer:#4a4a4a;
  --footer-dark:#3e3e3e;
  --white:#fff;
}
*{box-sizing:border-box;margin:0;padding:0}
html,body{width:1200px;height:3456px;overflow:hidden}
body{font-family:'Lato',sans-serif;color:var(--ink);background:var(--white);position:relative}
.abs{position:absolute}
.btn{position:absolute;background:var(--blue);color:var(--white);font-size:14px;display:flex;align-items:center;justify-content:center;box-shadow:0 2px 4px rgba(0,0,0,.15)}
.wordmark{position:absolute;display:flex;align-items:center;gap:10px;font-size:29px;font-weight:400;line-height:1;color:var(--blue);white-space:nowrap}
.wordmark .dot{width:10px;height:10px;background:currentColor}
.section-title{position:absolute;font-size:27px;font-weight:700;color:#555;border-left:3px solid var(--blue);padding-left:14px;line-height:1}
.section-title span{color:var(--blue-dark)}
.nav{position:absolute;left:0;top:83px;width:1200px;height:49px;background:var(--nav)}
.nav a{position:absolute;top:0;height:49px;line-height:49px;color:var(--white);font-size:14px;text-decoration:none}
.social{position:absolute;display:flex;gap:17px}
.social i{display:block;width:13px;height:13px;border-radius:50%;background:var(--white)}
.hero{position:absolute;left:0;top:132px;width:1200px;height:660px;background:linear-gradient(100deg,#6d7e96 0%,#c99aa6 28%,#9a8fa8 50%,#c5ccd8 75%,#e6e9ee 100%)}
.hero h1{position:absolute;top:248px;width:100%;text-align:center;color:var(--white);font-size:46px;font-weight:700}
.hero p{position:absolute;top:312px;left:260px;width:680px;text-align:center;color:var(--white);font-size:13px;line-height:23px}
.svc{position:absolute;width:260px;text-align:center}
.svc svg{display:block;margin:0 auto}
.svc h3{font-size:20px;font-weight:400;color:#555;margin-top:14px}
.svc p{font-size:13px;line-height:19.5px;color:var(--muted);margin-top:10px;font-weight:300}
.about{position:absolute;left:0;top:1535px;width:1200px;height:392px;background:var(--light)}
.about-photo{position:absolute;left:0;top:0;width:595px;height:392px;background:linear-gradient(90deg,#9a8a72 0%,#d8d0c2 45%,#eeeae3 100%)}
.about p{position:absolute;left:638px;top:134px;width:420px;font-size:13px;line-height:19.5px;color:var(--muted);font-weight:300}
.member{position:absolute;width:262px;text-align:center}
.member .photo{width:261px;height:260px;background:linear-gradient(160deg,#b9b3aa,#4a4f5c)}
.member h4{font-size:19px;font-weight:400;color:#555;margin-top:26px}
.member p{height:98px;font-size:13px;line-height:19.5px;color:var(--muted);margin-top:10px;font-weight:300;padding:0 12px}
.member a{display:block;margin-top:18px;font-size:14px;color:var(--blue);text-decoration:underline}
.arrow{position:absolute}
.consult{position:absolute;left:0;top:2667px;width:1200px;height:402px;background:var(--light)}
.card{position:absolute;left:666px;top:2637px;width:379px;height:464px;background:var(--white);box-shadow:0 0 10px rgba(0,0,0,.08)}
.card h2{text-align:center;font-size:26px;font-weight:400;color:#555;margin-top:36px}
.card h2 span{color:var(--blue-dark)}
.field{position:absolute;left:33px;width:317px;border-bottom:1px solid #9aa0b4;font-size:12px;color:#aaa;padding-bottom:10px}
.footer{position:absolute;left:0;top:3069px;width:1200px;height:387px;background:var(--footer);color:var(--white)}
.footer h5{position:absolute;top:96px;font-size:18px;font-weight:700}
.footer .txt{position:absolute;font-size:13px;line-height:19.5px}
.footer ul{position:absolute;list-style:none;font-size:13px;line-height:19.5px}
.footer li::before{content:"·";margin-right:12px}
.copy{position:absolute;left:12px;top:346px;width:1188px;height:41px;background:var(--footer-dark);font-size:13px;line-height:41px;padding-left:140px}
</style>
</head>
<body>

<header>
  <div class="wordmark" style="left:150px;top:24px"><span class="dot"></span>Tallow Field</div>
  <svg class="abs" style="left:783px;top:26px" width="20" height="20" viewBox="0 0 24 24"><path fill="#4a5cc4" d="M6.6 10.8a15 15 0 006.6 6.6l2.2-2.2c.3-.3.7-.4 1-.2 1.1.4 2.3.6 3.6.6.6 0 1 .4 1 1V20c0 .6-.4 1-1 1A17 17 0 013 4c0-.6.4-1 1-1h3.5c.6 0 1 .4 1 1 0 1.3.2 2.5.6 3.6.1.3 0 .7-.2 1z"/></svg>
  <div class="abs" style="left:817px;top:25px;font-size:11px;color:#aaa;line-height:15px">Call us now :<br><span style="color:var(--blue)">(555) 010-2141</span></div>
  <div class="btn" style="left:916px;top:19px;width:135px;height:40px">Free Consultation</div>
</header>

<nav class="nav">
  <a style="left:149px;width:87px;background:var(--blue);text-align:center">Home</a>
  <a style="left:260px">About us</a>
  <a style="left:371px">Services</a>
  <a style="left:476px">Our Team</a>
  <a style="left:587px">Contact us</a>
  <div class="social" style="left:901px;top:18px"><i></i><i></i><i></i><i></i><i></i></div>
</nav>

<section class="hero" role="img" aria-label="Photo of a lawyer at a desk with a gavel, blended with a city skyline">
  <h1>Great lawyers. Great law firm</h1>
  <p>Lorem Ipsum is simply dummy text of the printing and typesetting industry. Lorem Ipsum has been the industry's standard dummy text ever since the 1500s</p>
  <div class="btn" style="left:531px;top:383px;width:133px;height:39px">Free Consultation</div>
</section>

<section>
  <h2 class="section-title" style="left:514px;top:851px">Our <span>Services</span></h2>
  <div class="svc" style="left:142px;top:938px">
    <svg width="34" height="40" viewBox="0 0 34 40"><circle cx="17" cy="6" r="5" fill="#4a5cc4"/><path d="M4 10l9 7v10l-3 12h5l2-9 2 9h5l-3-12V17l9-7-3-3-8 6h-4L7 7z" fill="#4a5cc4"/></svg>
    <h3>Child Custody</h3>
    <p>Lorem Ipsum is simply dummy text of the printing and typesetting industry. Lorem Ipsum has been the industry's standard dummy text .</p>
  </div>
  <div class="svc" style="left:468px;top:938px">
    <svg width="40" height="40" viewBox="0 0 40 40"><path d="M20 3L2 18h5v19h26V18h5z" fill="#4a5cc4"/><path d="M20 31l-7-7a4 4 0 016-5l1 1 1-1a4 4 0 016 5z" fill="#fff"/></svg>
    <h3>Divorce</h3>
    <p>Lorem Ipsum is simply dummy text of the printing and typesetting industry. Lorem Ipsum has been the industry's standard dummy text .</p>
  </div>
  <div class="svc" style="left:796px;top:938px">
    <svg width="34" height="40" viewBox="0 0 34 40"><circle cx="20" cy="8" r="6" fill="#4a5cc4"/><path d="M8 16h16l4 10-4 4v8H8l-2-12z" fill="#4a5cc4"/><path d="M14 22h10v6H14z" fill="#fff"/></svg>
    <h3>Sex Crimes</h3>
    <p>Lorem Ipsum is simply dummy text of the printing and typesetting industry. Lorem Ipsum has been the industry's standard dummy text .</p>
  </div>
  <div class="svc" style="left:142px;top:1170px">
    <svg width="38" height="40" viewBox="0 0 38 40"><path d="M12 2h12l-4 7h-4z" fill="#4a5cc4"/><path d="M16 10h4c8 4 12 12 12 18 0 6-6 10-14 10S4 34 4 28c0-6 4-14 12-18z" fill="#4a5cc4"/><text x="18" y="31" font-size="15" font-family="Lato,sans-serif" fill="#fff" text-anchor="middle" font-weight="700">$</text></svg>
    <h3>Alimony</h3>
    <p>Lorem Ipsum is simply dummy text of the printing and typesetting industry. Lorem Ipsum has been the industry's standard dummy text .</p>
  </div>
  <div class="svc" style="left:468px;top:1170px">
    <svg width="34" height="40" viewBox="0 0 34 40"><path d="M5 4h24l-2 8H7z" fill="#4a5cc4"/><path d="M8 14h18v6c0 8-4 14-9 14s-9-6-9-14z" fill="#4a5cc4"/><path d="M10 18h14v3H10z" fill="#fff"/></svg>
    <h3>Fraud Crimes</h3>
    <p>Lorem Ipsum is simply dummy text of the printing and typesetting industry. Lorem Ipsum has been the industry's standard dummy text .</p>
  </div>
  <div class="svc" style="left:796px;top:1170px">
    <svg width="34" height="40" viewBox="0 0 34 40"><circle cx="18" cy="9" r="7" fill="#4a5cc4"/><path d="M8 18l18-2 2 8-8 4 2 10h-8l-4-10z" fill="#4a5cc4"/></svg>
    <h3>Domestic Violence</h3>
    <p>Lorem Ipsum is simply dummy text of the printing and typesetting industry. Lorem Ipsum has been the industry's standard dummy text .</p>
  </div>
  <div class="btn" style="left:522px;top:1429px;width:152px;height:41px">View More Services</div>
</section>

<section class="about">
  <div class="about-photo" role="img" aria-label="Bronze statue of Lady Justice with scales beside a wooden gavel near a bright window"></div>
  <h2 class="section-title" style="left:641px;top:89px">About <span>Us</span></h2>
  <p>The law firm of Tallow Field, LLC is based in Ashford County, conveniently located in Millbrook, New Jersey in 40 Harbor Plaza. We serve the needs of clients throughout Ashford County, as well as, clients from several other counties, including, but not limited to, Linden, Carver, Easton and Hale.</p>
  <div class="btn" style="left:633px;top:263px;width:134px;height:39px">Read More</div>
</section>

<section>
  <h2 class="section-title" style="left:540px;top:1989px">Our <span>Team</span></h2>
  <svg class="arrow" style="left:51px;top:2258px" width="52" height="52" viewBox="0 0 52 52"><circle cx="26" cy="26" r="24" fill="none" stroke="#ccc" stroke-width="2"/><path d="M36 26H16M24 18l-8 8 8 8" fill="none" stroke="#ccc" stroke-width="2"/></svg>
  <svg class="arrow" style="left:1096px;top:2258px" width="52" height="52" viewBox="0 0 52 52"><circle cx="26" cy="26" r="24" fill="none" stroke="#ccc" stroke-width="2"/><path d="M16 26h20M28 18l8 8-8 8" fill="none" stroke="#ccc" stroke-width="2"/></svg>
  <div class="member" style="left:164px;top:2071px">
    <div class="photo" role="img" aria-label="Portrait of attorney Daniel R. Tallow in a suit in his office"></div>
    <h4>Daniel R. Tallow</h4>
    <p>Daniel R. Tallow practices in the area of family law, specializing in high conflict matters relating to divorce, custody, equitable distribution, and complex financial issues.</p>
    <a>Read More</a>
  </div>
  <div class="member" style="left:469px;top:2071px">
    <div class="photo" role="img" aria-label="Portrait of attorney Marcus J. Field seated in a leather chair"></div>
    <h4>Marcus J. Field</h4>
    <p>Marcus J. Field is one of the founding partners of the firm. Mr. Field's primary concentration is in the areas of matrimonial, family law, appellate work, juvenile delinquency, crim.....</p>
    <a>Read More</a>
  </div>
  <div class="member" style="left:774px;top:2071px">
    <div class="photo" style="background:linear-gradient(160deg,#c7a79c,#3d3a3c)" role="img" aria-label="Portrait of associate Lena M. Ortiz outdoors in front of brick buildings"></div>
    <h4>Lena M. Ortiz</h4>
    <p>Lena Ortiz has been an associate at Tallow Field since 2016. In private practice, Ms. Ortiz focuses her practice on family and divorce law, which includes child custody and support matters...</p>
    <a>Read More</a>
  </div>
</section>

<section class="consult">
  <h2 class="section-title" style="left:157px;top:95px;border-left-color:#ccc;font-weight:400">Free Case <span>Evaluation</span></h2>
  <p class="abs" style="left:152px;top:144px;width:400px;font-size:13px;line-height:23px;color:#555">Lorem Ipsum is simply dummy text of the printing and typesetting industry. Lorem Ipsum has been the industry's standard dummy text ever since the 1500s.</p>
  <svg class="abs" style="left:153px;top:240px" width="20" height="20" viewBox="0 0 24 24"><path fill="#4a5cc4" d="M6.6 10.8a15 15 0 006.6 6.6l2.2-2.2c.3-.3.7-.4 1-.2 1.1.4 2.3.6 3.6.6.6 0 1 .4 1 1V20c0 .6-.4 1-1 1A17 17 0 013 4c0-.6.4-1 1-1h3.5c.6 0 1 .4 1 1 0 1.3.2 2.5.6 3.6.1.3 0 .7-.2 1z"/></svg>
  <div class="abs" style="left:182px;top:243px;font-size:13px;color:#555">Call us</div>
  <div class="abs" style="left:151px;top:263px;font-size:40px;color:var(--blue)">(555) 010-2141</div>
</section>

<form class="card">
  <h2>Get Free <span>Consultation</span></h2>
  <div class="field" style="top:106px">Full Name*</div>
  <div class="field" style="top:163px">Phone Number*</div>
  <div class="field" style="top:223px">Email Address*</div>
  <div class="field" style="top:278px;height:80px">Message*</div>
  <div class="btn" style="left:33px;top:395px;width:133px;height:39px">Submit Now</div>
</form>

<footer class="footer">
  <div class="wordmark" style="left:146px;top:100px;font-size:25px;color:var(--white)">Tallow Field</div>
  <p class="txt" style="left:150px;top:150px;width:230px">The law firm of Tallow Field, LLC is based in Ashford County, conveniently located in Millbrook, New Jersey in 40 Harbor Plaza.</p>
  <a class="txt" style="left:150px;top:275px;text-decoration:underline">Read More</a>

  <h5 style="left:431px">Quick Links</h5>
  <ul style="left:431px;top:150px"><li>Home</li><li>About us</li><li>Services</li><li>Our Team</li><li>Contact us</li></ul>

  <h5 style="left:590px">Contact us</h5>
  <svg class="abs" style="left:590px;top:153px" width="12" height="16" viewBox="0 0 12 16"><path d="M6 0a6 6 0 00-6 6c0 4 6 10 6 10s6-6 6-10a6 6 0 00-6-6zm0 8a2 2 0 110-4 2 2 0 010 4z" fill="#fff"/></svg>
  <p class="txt" style="left:613px;top:150px;width:200px">Tallow &amp; Field LLC<br>40 Harbor Plaza Drive Suite<br>312 Millbrook, NJ 07000</p>
  <svg class="abs" style="left:588px;top:228px" width="14" height="14" viewBox="0 0 24 24"><path fill="#fff" d="M6.6 10.8a15 15 0 006.6 6.6l2.2-2.2c.3-.3.7-.4 1-.2 1.1.4 2.3.6 3.6.6.6 0 1 .4 1 1V20c0 .6-.4 1-1 1A17 17 0 013 4c0-.6.4-1 1-1h3.5c.6 0 1 .4 1 1 0 1.3.2 2.5.6 3.6.1.3 0 .7-.2 1z"/></svg>
  <p class="txt" style="left:613px;top:225px">(555) 010-2141<br>(555) 010-1257</p>
  <svg class="abs" style="left:588px;top:248px" width="14" height="14" viewBox="0 0 14 14"><rect x="1" y="4" width="12" height="9" fill="#fff"/><rect x="3" y="1" width="8" height="4" fill="none" stroke="#fff"/></svg>

  <h5 style="left:843px">Free Consulation</h5>
  <p class="txt" style="left:845px;top:148px;width:210px">Lorem Ipsum is simply dummy text of the printing and typesetting industry.</p>
  <div class="btn" style="left:845px;top:246px;width:181px;height:41px">Request Consultation</div>

  <div class="copy">Copyright © 2020 Tallow &amp; Field, LLC.
    <div class="social" style="left:897px;top:14px"><i></i><i></i><i></i><i></i><i></i></div>
  </div>
</footer>

</body>
</html>
```